Melissa Dorvan Personal Business Card

I like orange. It's would better if my card have an orange background
Address: 5820 Halvers Lane #417
San Jose
California
US
Tel: 4085172049

Industry/Entity Type

Business

```html
<!DOCTYPE html>
<html lang="en">
<head>
<meta charset="utf-8">
<title>Melissa Dorvan – Business Card</title>
<link rel="stylesheet" href="https://fonts.googleapis.com/css2?family=Ubuntu:wght@700&family=Exo+2:wght@400&display=swap">
<style>
  :root {
    --brand-orange: #ff4800;
    --ink: #1e1e1e;
    --paper: #ffffff;
  }
  * { margin: 0; padding: 0; box-sizing: border-box; }
  html, body {
    width: 1200px;
    height: 686px;
    overflow: hidden;
    background: var(--paper);
  }
  .card {
    position: relative;
    width: 1200px;
    height: 686px;
    background: var(--paper);
    color: var(--ink);
  }
  .header-band {
    position: absolute;
    left: 0; top: 0;
    width: 100%;
    height: 198px;
    background: var(--brand-orange);
    display: flex;
    align-items: center;
    justify-content: center;
  }
  .holder-name {
    font-family: "Ubuntu", sans-serif;
    font-weight: 700;
    font-size: 92px;
    letter-spacing: 0.5px;
    color: var(--ink);
    line-height: 1;
    padding-bottom: 6px;
  }
  .footer-band {
    position: absolute;
    left: 0; bottom: 0;
    width: 100%;
    height: 63px;
    background: var(--brand-orange);
  }
  .contact-line {
    position: absolute;
    left: 287px;
    font-family: "Exo 2", sans-serif;
    font-weight: 400;
    font-size: 46px;
    line-height: 1;
    color: var(--ink);
    white-space: nowrap;
  }
  .address-street { top: 322px; }
  .address-city { top: 383px; }
  .address-region { top: 437px; }
  .phone-number { top: 491px; }
  .icon {
    position: absolute;
    fill: var(--brand-orange);
  }
  .icon-pin { left: 229px; top: 323px; width: 41px; height: 54px; }
  .icon-phone { left: 232px; top: 476px; width: 34px; height: 55px; }
</style>
</head>
<body>
  <main class="card">
    <header class="header-band">
      <h1 class="holder-name">Melissa Dorvan</h1>
    </header>

    <svg class="icon icon-pin" viewBox="0 0 41 54" aria-hidden="true">
      <path d="M20.5 0C9.2 0 0 9 0 20.2 0 33 20.5 54 20.5 54S41 33 41 20.2C41 9 31.8 0 20.5 0Zm0 27.5a7.6 7.6 0 1 1 0-15.2 7.6 7.6 0 0 1 0 15.2Z"/>
    </svg>
    <p class="contact-line address-street">5820 Halvers Lane #417</p>
    <p class="contact-line address-city">San Jose</p>
    <p class="contact-line address-region">California -U S</p>

    <svg class="icon icon-phone" viewBox="0 0 34 55" aria-hidden="true">
      <rect x="3" y="0" width="4" height="12" rx="2"/>
      <path d="M7 9h20a7 7 0 0 1 7 7v32a7 7 0 0 1-7 7H7a7 7 0 0 1-7-7V16a7 7 0 0 1 7-7Zm1 7a2 2 0 0 0-2 2v12a2 2 0 0 0 2 2h18a2 2 0 0 0 2-2V18a2 2 0 0 0-2-2Zm9 25a3.6 3.6 0 1 0 0 7.2 3.6 3.6 0 0 0 0-7.2Z" fill-rule="evenodd"/>
    </svg>
    <p class="contact-line phone-number">4085172049</p>

    <footer class="footer-band"></footer>
  </main>
</body>
</html>
```